| バナーサイズ |
| 現在のヘッダーデザインにとらわれず、サイトイメージとマッチするような、 オリジナルのヘッダーを作成して下さい。 ■サイズ ヘッダー画像サイズ:横幅1450px、縦幅680px 対象サイト:http://www.verdant-k.example ■会社(サービス)概要 企業向けのコンサルティングサービス、各種ビジネスサービスを展開しています。 主に中小企業、中堅企業向けのクライアントが対象 ■利用客層 男性メイン 特に、課長/部長等のマネージメントクラス、役員/経営者向け ■最後に ご質問あれば、回答させて頂きます。 一人で複数の応募も問題ございません。 多くの方からの、ご応募をお待ちしています。 |

```html
<!DOCTYPE html>
<html lang="ja">
<head>
<meta charset="UTF-8">
<title>Verdant Group ヘッダー</title>
<link rel="stylesheet" href="https://fonts.googleapis.com/css2?family=Noto+Sans+JP:wght@400;500;700;900&family=Noto+Serif+JP:wght@500;700&display=swap">
<style>
  :root {
    --navy: #1c2a6b;
    --ink: #2b2b2b;
    --nav-ink: #3a4a8a;
    --white: #ffffff;
    --sky-1: #eaf4fb;
    --sky-2: #a9d2ec;
    --sky-3: #5c9fd0;
    --sky-4: #2f6fa8;
    --page: #ffffff;
  }
  * { margin: 0; padding: 0; box-sizing: border-box; }
  html, body { width: 1200px; height: 934px; overflow: hidden; background: var(--page); }
  body { font-family: "Noto Sans JP", sans-serif; color: var(--ink); position: relative; }

  .site-header {
    position: absolute; left: 0; top: 0; width: 1200px; height: 150px;
    background: var(--white);
  }
  .brand {
    position: absolute; left: 112px; top: 30px; width: 180px;
    display: flex; flex-direction: column; align-items: flex-start; gap: 8px;
  }
  .brand-dot { width: 52px; height: 52px; border-radius: 50%; background: var(--navy); }
  .brand-name {
    font-family: "Noto Serif JP", serif; font-weight: 700; font-size: 18px;
    color: var(--navy); line-height: 1.2; white-space: nowrap;
  }
  .global-nav {
    position: absolute; left: 343px; top: 52px; width: 690px;
    display: flex; justify-content: space-between;
  }
  .global-nav a {
    font-size: 14px; font-weight: 500; color: var(--nav-ink); text-decoration: none; white-space: nowrap;
  }

  .hero {
    position: absolute; left: 0; top: 150px; width: 1200px; height: 570px;
    overflow: hidden;
  }
  .hero-visual {
    position: absolute; inset: 0;
    background:
      radial-gradient(ellipse 40% 60% at 30% 55%, rgba(47,111,168,0.55), transparent 70%),
      radial-gradient(ellipse 35% 55% at 75% 50%, rgba(47,111,168,0.5), transparent 70%),
      radial-gradient(ellipse 50% 40% at 50% 20%, rgba(255,255,255,0.9), transparent 70%),
      linear-gradient(180deg, var(--sky-1) 0%, var(--sky-2) 45%, var(--sky-3) 80%, var(--sky-2) 100%);
  }
  .hero-copy {
    position: absolute; left: 0; right: 0; top: 200px; text-align: center; color: var(--white);
  }
  .hero-title {
    font-weight: 900; font-size: 66px; letter-spacing: 0.04em; line-height: 1.1;
    text-shadow: 0 2px 8px rgba(20,50,100,0.55);
  }
  .hero-lead {
    margin-top: 16px;
    font-family: "Noto Serif JP", serif; font-weight: 700; font-size: 23px;
    text-shadow: 0 1px 5px rgba(20,50,100,0.7);
  }

  .mission {
    position: absolute; left: 0; top: 720px; width: 1200px; height: 214px;
    background: var(--white);
    padding-top: 48px; text-align: center;
  }
  .mission-text {
    font-size: 31px; font-weight: 400; line-height: 1.65; color: var(--ink);
  }
</style>
</head>
<body>
  <header class="site-header">
    <div class="brand">
      <span class="brand-dot"></span>
      <span class="brand-name">Verdant Group</span>
    </div>
    <nav class="global-nav">
      <a href="#">サービス一覧</a>
      <a href="#">お客様の成功事例</a>
      <a href="#">blog</a>
      <a href="#">会社概要</a>
      <a href="#">お問い合わせ</a>
    </nav>
  </header>

  <section class="hero">
    <div class="hero-visual" role="img" aria-label="青いトーンで重ねたビジネスパーソンのシルエットと都市の風景写真"></div>
    <div class="hero-copy">
      <h1 class="hero-title">今を変えて、未来を創る。</h1>
      <p class="hero-lead">実践型エキスパートが、戦略的事業創造と新産業創出をハンズオンで支援</p>
    </div>
  </section>

  <section class="mission">
    <p class="mission-text">私たちは事業の課題を明確にし、解決するプロセスで組織の<br>成長とイノベーションを成し遂げます。</p>
  </section>
</body>
</html>
```